Form Crafters Business Card

Professional cosmetic surgery company, based in very exclusive area in London. High profiled clientele. Brand is very artistic, modern, state-of-the-art, safe. The best in the business. Celebrity clientele.

Form Crafter’s of London is a brand serving a discriminating and exclusive clientele who value personal service that is both intimate and high end. Our clients choose Form Crafters because of the relationships we share with all of our customers. The clients of Form Crafters have an equal partnership between customers, and very experienced, highly qualified medical professionals. This together provides you with a professional service that keeps you looking good and feeling good. It is a relationship based on honesty, compassion, loyalty and respect.
Form Crafter’s have provided services for internationally recognised celebrities, and other high profiled individuals.

The cards are used for networking at private, exclusive events with VIPs.

Target Market(s)

Professionals
Rich people

Industry/Entity Type

Professional Service

Contact Information for Business Card

Need double sided business card design for 4 people. Back of the business card needs to have contrast background to the front with butterfly watermark with services provided:
Hair Restoration surgery
Hair Loss treatments
Breast surgery
Rhinoplasty
Zelix Liposuction
Fat Grafting
Lumex & Fillers

Front of the business card needs to be a nice satin black.
with following information:
Talvan Desoruthy - name
Chief Executive - Job title

www.formcrafters-example.co.uk
talvan@formcrafters-example.co.uk
Phone: +44 (0)207 146 5327
Mobile: +44 (0)7491 825 436

The London Calder Infirmary
14 Pellmont Street | London | W1K 3TR
Off Dunmore Lane

All business cards have the same address, phone, website as Talvan's details.
Same details on the back of the business card as well.
The other cards have different name, job title, email, mobile number

Kerem Lutz - Name
Partner - Job Title
Former England International Cricketer - please include below job title

email: kerem@formcrafters-example.co.uk
mobile: +44(0)7862 514208

Dr Stellan Vastrel - Name
Plastic Surgeon - Job Title
drvastrel@formcrafters-example.co.uk
No mobile number

Dr Jon Torvick FRCS (please put FRCS in small font) - Name
Hair Restoration Surgeon - Job Title
drtorvick@formcrafters-example.co.uk
No mobile number

Colors
cedeec
85abd2
0655a3

Requirements
Must have
• The logo needs to be in a metallic finish
• Text needs to be striking
• nice background
• butterfly watermark on the back

```html
<!DOCTYPE html>
<html lang="en">
<head>
<meta charset="utf-8">
<title>Form Crafters Business Card</title>
<link href="https://fonts.googleapis.com/css2?family=Josefin+Slab:wght@400;600;700&display=swap" rel="stylesheet">
<style>
  :root {
    --stage: #1b1b1b;
    --satin-black: #0c0c0d;
    --satin-sheen: #1d1e21;
    --orange: #f7931e;
    --orange-deep: #ef5a24;
    --blue: #0655a3;
    --blue-mid: #85abd2;
    --ice: #cedeec;
    --white: #ffffff;
    --ink: #1a1a1a;
    --grey: #6d6d6d;
    --light-grey: #c9c9c9;
  }
  * { box-sizing: border-box; margin: 0; padding: 0; }
  html, body { width: 1200px; height: 1000px; overflow: hidden; }
  body {
    background: var(--stage);
    font-family: "Josefin Slab", Georgia, serif;
    position: relative;
  }
  .card {
    position: absolute;
    top: 351px;
    width: 520px;
    height: 298px;
    border-radius: 4px;
    overflow: hidden;
    box-shadow: 0 10px 30px rgba(0,0,0,.5);
  }
  /* Back side: services */
  .card--services {
    left: 60px;
    background: linear-gradient(135deg, var(--satin-sheen) 0%, var(--satin-black) 55%, #050505 100%);
  }
  .brand {
    position: absolute;
    left: 52px;
    top: 52px;
    display: flex;
    align-items: center;
    gap: 12px;
  }
  .brand__dot {
    width: 30px; height: 30px; border-radius: 50%;
    background: var(--blue);
  }
  .brand__name {
    font-size: 34px;
    font-weight: 600;
    color: var(--blue-mid);
    letter-spacing: 1px;
    line-height: 1;
  }
  .brand__tagline {
    position: absolute;
    left: 94px; top: 96px;
    font-size: 11px;
    font-weight: 600;
    letter-spacing: 1.5px;
    color: var(--orange);
    text-transform: uppercase;
  }
  .services {
    position: absolute;
    left: 52px; top: 138px;
    list-style: none;
    color: var(--orange);
    font-size: 19px;
    line-height: 21px;
  }
  .services__web {
    position: absolute;
    right: 28px; bottom: 28px;
    color: var(--white);
    font-size: 12px;
    letter-spacing: 1.5px;
  }
  /* Front side: contact */
  .card--contact {
    left: 620px;
    background: var(--white);
  }
  .contact__top {
    position: absolute;
    left: 0; top: 0; width: 100%; height: 162px;
    background: linear-gradient(135deg, var(--satin-sheen) 0%, var(--satin-black) 70%);
  }
  .contact__band {
    position: absolute;
    left: 0; top: 162px; width: 100%; height: 7px;
    background: linear-gradient(90deg, var(--orange-deep), var(--orange) 60%, #fbb03b);
  }
  .person {
    position: absolute;
    left: 36px; top: 30px;
    color: var(--light-grey);
  }
  .person__name { font-size: 22px; font-weight: 700; color: var(--orange); }
  .person__title { font-size: 14px; margin-top: 4px; color: #9a9a9a; }
  .person__email { font-size: 14px; margin-top: 26px; }
  .person__mobile { font-size: 14px; margin-top: 4px; }
  .address {
    position: absolute;
    left: 36px; top: 186px;
    color: var(--grey);
    font-size: 14px;
    line-height: 19px;
  }
  .address__venue {
    color: var(--ink);
    font-size: 15px;
    font-weight: 600;
    text-transform: uppercase;
    letter-spacing: .5px;
    margin-bottom: 2px;
  }
  .address__web { color: var(--orange-deep); letter-spacing: 1.5px; }
</style>
</head>
<body>
  <section class="card card--services">
    <div class="brand">
      <span class="brand__dot"></span>
      <span class="brand__name">Form Crafters</span>
    </div>
    <div class="brand__tagline">Refined care, lasting confidence</div>
    <ul class="services">
      <li>Hair Restoration surgery</li>
      <li>Hair Loss treatments</li>
      <li>Breast surgery</li>
      <li>Rhinoplasty</li>
      <li>Zelix Liposuction</li>
      <li>Fat Grafting Lumex &amp; Fillers</li>
    </ul>
    <div class="services__web">www.formcrafters-example.co.uk</div>
  </section>

  <section class="card card--contact">
    <div class="contact__top"></div>
    <div class="contact__band"></div>
    <div class="person">
      <div class="person__name">Talvan Desoruthy</div>
      <div class="person__title">Chief Executive</div>
      <div class="person__email">talvan@formcrafters-example.co.uk</div>
      <div class="person__mobile">+44 (0)7491 825 436</div>
    </div>
    <div class="address">
      <div class="address__venue">The London Calder Infirmary</div>
      <div>14 Pellmont Street, London</div>
      <div>W1K 3TR Off Dunmore Lane</div>
      <div>+44 (0)207 146 5327</div>
      <div class="address__web">www.formcrafters-example.co.uk</div>
    </div>
  </section>
</body>
</html>
```